OREV - Helping People with Disabilities

OREV is a nonprofit that strives to enable people with physical disabilities to live meaningful, quality lives. OREV needs a professional attractive website that:
• establishes a strong brand image
• presents Orev's services to those who need it
• raises funds from potential donors
Please see WORD DOC attached for more information about design vision.

Target Market(s)

people with disabilities

Industry/Entity Type

charity website

Number of Pages Required

2 page

Font styles to use
Sans Serif

Requirements
Must have
• 1. 2 pages means 1 design for homepage and 1 design for top of inner pages (banner ideas)
Nice to have
• please see attached design brief (WORD DOC)

```html
<!DOCTYPE html>
<html lang="en">
<head>
<meta charset="utf-8">
<title>OREV – A Good Life for Everyone</title>
<link href="https://fonts.googleapis.com/css2?family=Exo+2:wght@500;600;700&family=Poppins:wght@400;500;600&display=swap" rel="stylesheet">
<style>
:root{
  --teal:#0f6b64;
  --teal-dark:#0c5a54;
  --green:#1db04b;
  --cyan:#18bcc4;
  --gray:#666a6b;
  --light:#f4f6f6;
  --text:#3b3f40;
  --white:#fff;
}
*{box-sizing:border-box;margin:0;padding:0}
html,body{width:1200px;height:4027px;overflow:hidden;background:var(--white)}
body{position:relative;font-family:"Poppins",sans-serif;color:var(--text)}
.abs{position:absolute}
h1,h2,h3,.display{font-family:"Exo 2",sans-serif}
.btn{position:absolute;display:flex;align-items:center;justify-content:center;font:600 11px "Poppins",sans-serif;color:var(--white);background:var(--green);border-radius:2px}
.btn--teal{background:var(--teal)}
.eyebrow{font:600 13px "Poppins",sans-serif;color:var(--green)}

/* header */
.logo{left:164px;top:50px;display:flex;align-items:center;gap:8px;font:700 30px "Exo 2",sans-serif;color:var(--teal)}
.logo__dot{width:14px;height:14px;background:var(--green);border-radius:50%}
.topbar{left:530px;top:63px;display:flex;align-items:center;gap:16px;font-size:11px;color:#555}
.topbar__call{color:var(--green);font-weight:600}
.topbar__call b{color:var(--teal);margin-left:6px}
.topbar__sep{color:#bbb}
.social{display:flex;gap:8px}
.social span{width:24px;height:24px;border-radius:50%;background:var(--green)}
.lang{width:24px;height:24px;border-radius:50%;border:1.5px solid #999;font-size:8px;display:flex;align-items:center;justify-content:center;margin-left:18px}
.nav{left:368px;top:103px;display:flex;gap:28px;font-size:11px;font-weight:500;color:#333}
.nav a{text-decoration:none;color:inherit}
.nav .is-active{color:var(--green)}

/* hero */
.hero{left:35px;top:149px;width:1130px;height:498px;
  background:radial-gradient(ellipse at 45% 40%,#8a5a35 0,#4f6a3a 22%,#3d5d35 45%,#2f4a2e 75%,#263c26 100%);
  clip-path:polygon(0 0,100% 0,100% 449px,83% 498px,17% 498px,0 449px)}
.hero__shade{left:35px;top:149px;width:1130px;height:498px;background:rgba(10,30,20,.25);clip-path:polygon(0 0,100% 0,100% 449px,83% 498px,17% 498px,0 449px)}
.hero__title{left:0;width:1200px;top:290px;text-align:center;color:var(--white);font:600 40px/52px "Exo 2",sans-serif}
.hero__know{left:0;width:1200px;top:562px;text-align:center;color:var(--white);font:500 15px "Poppins",sans-serif}
.hero__lines{left:35px;top:590px}

.card{position:absolute;top:631px;width:172px;height:196px;display:flex;flex-direction:column;align-items:center;padding:24px 16px 0;text-align:center;color:var(--white);font-size:11px;line-height:18px}
.card svg{margin-bottom:22px}
.card--teal{background:var(--teal)}
.card--green{background:var(--green);box-shadow:0 6px 14px rgba(0,0,0,.18)}
.card--cyan{background:var(--cyan)}
.card--gray{background:var(--gray)}

/* about */
.about__eyebrow{left:223px;top:937px}
.about__title{left:223px;top:968px;font-size:27px;font-weight:700;color:var(--teal)}
.about__text{left:223px;top:1025px;width:368px;font-size:10px;line-height:17.5px;color:#444}
.about__text p+p{margin-top:14px}
.about__btn{left:223px;top:1229px;width:106px;height:31px}
.about__media{left:611px;top:882px}

/* services */
.services{left:35px;top:1333px;width:1130px;height:558px;background:var(--teal)}
.services__eyebrow{left:0;width:1200px;top:1402px;text-align:center;color:var(--white);font:500 13px "Poppins",sans-serif}
.services__title{left:0;width:1200px;top:1430px;text-align:center;color:var(--white);font-size:27px;font-weight:600}
.service{position:absolute;top:1492px;width:182px;color:var(--white)}
.service__img{width:182px;height:147px}
.service h3{font:500 14px/17px "Poppins",sans-serif;margin-top:30px}
.service p{font-size:9.5px;line-height:18px;margin-top:18px;height:70px;opacity:.9}
.service .more{font-size:10px;font-weight:600;margin-top:16px}
.service__rule{position:absolute;top:1492px;width:1px;height:345px;background:rgba(255,255,255,.18)}

.slogan{left:35px;top:1891px;width:1130px;height:265px;background:linear-gradient(180deg,var(--cyan) 0,#13a9a5 100%)}
.slogan__title{left:0;width:1200px;top:1952px;text-align:center;color:var(--white);font:600 33px/43px "Exo 2",sans-serif}
.slogan__btn{left:503px;top:2060px;width:192px;height:31px}

/* branches */
.branches{left:35px;top:2156px;width:1130px;height:490px;background:var(--light)}
.branches__eyebrow{left:223px;top:2265px}
.branches__title{left:223px;top:2292px;font-size:27px;font-weight:600;color:var(--teal)}
.branch-list{position:absolute;top:2346px;list-style:none;font-size:10px;font-weight:500;color:#333}
.branch-list li{height:27px;display:flex;align-items:center;gap:12px}
.branches__btn{left:223px;top:2505px;width:106px;height:31px}
.branches__frame{left:611px;top:2227px;width:365px;height:352px;border:2px solid var(--green);padding:10px;background:var(--white)}
.branches__img{width:100%;height:100%;background:linear-gradient(160deg,#8fb9d9 0,#4d86c5 45%,#3e9b4a 90%)}

/* news */
.news__eyebrow{left:0;width:1200px;top:2716px;text-align:center}
.news__title{left:0;width:1200px;top:2740px;text-align:center;font-size:27px;font-weight:600;color:var(--teal)}
.article{position:absolute;top:2795px;width:235px;height:341px;background:var(--white);box-shadow:0 4px 14px rgba(0,0,0,.08)}
.article__img{height:157px}
.article__body{padding:22px 16px 0}
.article h3{font:500 14px/18px "Exo 2",sans-serif;color:var(--teal)}
.article p{font-size:9.5px;line-height:18px;margin-top:16px;color:#444}
.article .more{font-size:10px;font-weight:600;color:var(--green);margin-top:18px}
.news__btn{left:547px;top:3169px;width:106px;height:31px}

/* footer */
.footer{left:35px;top:3606px;width:1130px;height:404px;background:var(--teal);clip-path:polygon(0 31px,247px 0,100% 0,100% 100%,0 100%)}
.quote{left:282px;top:3259px;width:635px;height:387px;background:var(--green)}
.quote__eyebrow{left:0;width:1200px;top:3306px;text-align:center;color:var(--white);font:500 12px "Poppins",sans-serif}
.quote__title{left:0;width:1200px;top:3326px;text-align:center;color:var(--white);font-size:27px;font-weight:600}
.field{position:absolute;background:var(--white);font-size:9px;color:var(--teal);padding:9px 14px}
.quote__btn{left:547px;top:3555px;width:106px;height:31px;background:var(--teal)}

.footer__logo{left:223px;top:3760px;display:flex;align-items:center;gap:10px;font:700 40px "Exo 2",sans-serif;color:var(--white)}
.footer__logo span{width:16px;height:16px;background:var(--green);border-radius:50%}
.footer__head{font:500 12px "Poppins",sans-serif;color:var(--green)}
.footer__col{position:absolute;top:3716px;color:var(--white);font-size:10px}
.footer__contact li{list-style:none;display:flex;gap:12px;margin-top:14px;line-height:17px}
.footer__links{list-style:none;line-height:21px;margin-top:12px}
.footer__social{display:flex;gap:10px;margin-top:20px}
.footer__social span{width:28px;height:28px;border-radius:50%;background:var(--green)}
.copyright{left:223px;top:3946px;color:var(--white);font-size:9.5px}
</style>
</head>
<body>

<!-- header -->
<div class="abs logo"><span class="logo__dot"></span>OREV</div>
<div class="abs topbar">
  <span class="topbar__call">Call Us Today <b>03-5550142</b></span>
  <span class="topbar__sep">|</span><span>Shop</span><span class="topbar__sep">|</span><span>Joining OREV</span>
  <div class="social" style="margin-left:20px"><span></span><span></span><span></span></div>
  <span class="lang">EN</span>
</div>
<nav class="abs nav">
  <a class="is-active">- Home -</a><a>About</a><a>Programs</a><a>Rehabilitation &amp; Sports</a><a>Rights Realization</a><a>News</a><a>Contact Us</a>
</nav>
<div class="btn" style="left:917px;top:94px;width:118px;height:35px">Donation to Orev</div>

<!-- hero -->
<div class="abs hero" role="img" aria-label="Photo of an adult hand passing a basketball to a smiling girl in a wheelchair outdoors"></div>
<div class="abs hero__shade"></div>
<h1 class="abs hero__title">A Good Life for Everyone,<br>Like Everyone</h1>
<div class="btn" style="left:496px;top:408px;width:208px;height:31px">Donate to Help Us Help Them</div>
<div class="abs hero__know">I Want to Know:</div>
<svg class="abs hero__lines" width="1130" height="70" viewBox="0 0 1130 70">
  <polyline points="0,12 188,60" fill="none" stroke="#ffffff" stroke-width="2"/>
  <polyline points="0,20 188,66" fill="none" stroke="#1db04b" stroke-width="2"/>
  <polyline points="1130,12 942,60" fill="none" stroke="#ffffff" stroke-width="2"/>
  <polyline points="1130,20 942,66" fill="none" stroke="#1db04b" stroke-width="2"/>
</svg>

<div class="card card--teal" style="left:223px">
  <svg width="30" height="30" viewBox="0 0 30 30" fill="none" stroke="#fff" stroke-width="2"><circle cx="15" cy="5" r="3"/><path d="M13 10v9h8l3 7M11 14a7 7 0 1 0 9 9"/></svg>
  What are all the rights available to people with physical disabilities and their families?
</div>
<div class="card card--green" style="left:417px">
  <svg width="30" height="30" viewBox="0 0 30 30" fill="none" stroke="#fff" stroke-width="2"><path d="M7 2h12l5 5v21H7z"/><path d="M13 12v9l7-4.5z" fill="#fff"/></svg>
  Where I can join online classes offered by OREV?
</div>
<div class="card card--cyan" style="left:611px">
  <svg width="30" height="30" viewBox="0 0 30 30" fill="none" stroke="#fff" stroke-width="2"><circle cx="19" cy="5" r="3"/><path d="M17 10l-4 8 5 3-3 7M13 18l-6 3M17 10l6 4"/></svg>
  What services there are for children with disabilities?
</div>
<div class="card card--gray" style="left:805px">
  <svg width="30" height="30" viewBox="0 0 30 30" fill="none" stroke="#fff" stroke-width="2"><rect x="6" y="3" width="18" height="24"/><path d="M10 8h3M17 8h3M10 13h3M17 13h3M10 18h3M17 18h3M13 27v-4h4v4"/></svg>
  If there is a rehabilitation center in my area?
</div>

<!-- about -->
<div class="abs eyebrow about__eyebrow">Who we are</div>
<h2 class="abs about__title">What is the Orev association?</h2>
<div class="abs about__text">
  <p>The Orev association is one of the oldest associations in Israel, which works to create support systems to integrate children and adults with disabilities, as independent and equal in the general Israeli society. In its vision, Orev believes in providing a meaningful and high-quality life to people with physical disabilities</p>
  <p>The association was founded in 1952 by volunteers who wanted to deal with polio victims. Since then, the association's activities have expanded and today, the association operates activity frameworks under tenders of the Ministry of Welfare and Social Security ...</p>
</div>
<div class="btn btn--teal about__btn">Explore More</div>
<svg class="abs about__media" width="365" height="353" viewBox="0 0 365 353">
  <polygon points="182,0 365,310 0,310" fill="#0f6b64"/>
  <polygon points="182,40 330,353 34,353" fill="#8fb8c9" role="img" aria-label="Photo of a man in a wheelchair chatting with a friend by the sea"/>
  <polygon points="182,40 330,353 34,353" fill="url(#sea)"/>
  <defs><linearGradient id="sea" x1="0" y1="0" x2="0" y2="1"><stop offset="0" stop-color="#a9cfe0"/><stop offset=".55" stop-color="#6e95a6"/><stop offset="1" stop-color="#b9a890"/></linearGradient></defs>
</svg>

<!-- services -->
<div class="abs services"></div>
<div class="abs services__eyebrow">Our Services</div>
<h2 class="abs services__title">What we offer you</h2>

<div class="service" style="left:164px">
  <div class="service__img" role="img" aria-label="Photo of a teacher and children at a learning table" style="background:linear-gradient(150deg,#e9d7c5,#c98e6a 55%,#8a5a48)"></div>
  <h3>Education<br>Orev</h3>
  <p>Works to impart education and knowledge to people with disabilities and operates the dedicated campus ...</p>
  <div class="more">Read More →</div>
</div>
<div class="service__rule" style="left:370px"></div>
<div class="service" style="left:394px">
  <div class="service__img" role="img" aria-label="Photo of a physiotherapy session with a trainer" style="background:linear-gradient(150deg,#f0f0f0,#c9ccd2 55%,#6a7fa8)"></div>
  <h3>Sports and Rehab<br>Orev</h3>
  <p>Encourages people with disabilities to play sports and find new strengths in themselves...</p>
  <div class="more">Read More →</div>
</div>
<div class="service__rule" style="left:599px"></div>
<div class="service" style="left:623px">
  <div class="service__img" role="img" aria-label="Photo of a lawyer's desk with scales and documents" style="background:linear-gradient(150deg,#3c3c3c,#7a6a58 55%,#2a2a2a)"></div>
  <h3>Rights Realization<br>Orev</h3>
  <p>Promotes policies concerning people with physical-motor disabilities, promotes their rights, ...</p>
  <div class="more">Read More →</div>
</div>
<div class="service__rule" style="left:828px"></div>
<div class="service" style="left:852px">
  <div class="service__img" role="img" aria-label="Photo of volunteers unpacking boxes at a community center" style="background:linear-gradient(150deg,#e6eaee,#9fb0bf 55%,#6f7d6a)"></div>
  <h3>Community Infrastructure<br>Orev</h3>
  <p>Owns the association's houses all over the country, rehabilitation day centers...</p>
  <div class="more">Read More →</div>
</div>

<div class="abs slogan"></div>
<h2 class="abs slogan__title">Even people with disabilities can be<br>with everyone, like everyone</h2>
<div class="btn slogan__btn">Don't Leave Them Behind</div>

<!-- branches -->
<div class="abs branches"></div>
<div class="abs eyebrow branches__eyebrow">Orev</div>
<h2 class="abs branches__title">Branch list</h2>
<ul class="branch-list" style="left:223px">
  <li><svg width="8" height="11" viewBox="0 0 8 11"><path d="M4 0a4 4 0 0 1 4 4c0 3-4 7-4 7S0 7 0 4a4 4 0 0 1 4-4z" fill="#1db04b"/></svg>Merhav-Hasharon</li>
  <li><svg width="8" height="11" viewBox="0 0 8 11"><path d="M4 0a4 4 0 0 1 4 4c0 3-4 7-4 7S0 7 0 4a4 4 0 0 1 4-4z" fill="#1db04b"/></svg>Eilat</li>
  <li><svg width="8" height="11" viewBox="0 0 8 11"><path d="M4 0a4 4 0 0 1 4 4c0 3-4 7-4 7S0 7 0 4a4 4 0 0 1 4-4z" fill="#1db04b"/></svg>Bat Yam</li>
  <li><svg width="8" height="11" viewBox="0 0 8 11"><path d="M4 0a4 4 0 0 1 4 4c0 3-4 7-4 7S0 7 0 4a4 4 0 0 1 4-4z" fill="#1db04b"/></svg>Netania</li>
  <li><svg width="8" height="11" viewBox="0 0 8 11"><path d="M4 0a4 4 0 0 1 4 4c0 3-4 7-4 7S0 7 0 4a4 4 0 0 1 4-4z" fill="#1db04b"/></svg>Beer-Sheva</li>
</ul>
<ul class="branch-list" style="left:370px">
  <li><svg width="8" height="11" viewBox="0 0 8 11"><path d="M4 0a4 4 0 0 1 4 4c0 3-4 7-4 7S0 7 0 4a4 4 0 0 1 4-4z" fill="#1db04b"/></svg>Bnei Brak</li>
  <li><svg width="8" height="11" viewBox="0 0 8 11"><path d="M4 0a4 4 0 0 1 4 4c0 3-4 7-4 7S0 7 0 4a4 4 0 0 1 4-4z" fill="#1db04b"/></svg>Hedera</li>
  <li><svg width="8" height="11" viewBox="0 0 8 11"><path d="M4 0a4 4 0 0 1 4 4c0 3-4 7-4 7S0 7 0 4a4 4 0 0 1 4-4z" fill="#1db04b"/></svg>Ashdod - Ashkelon</li>
  <li><svg width="8" height="11" viewBox="0 0 8 11"><path d="M4 0a4 4 0 0 1 4 4c0 3-4 7-4 7S0 7 0 4a4 4 0 0 1 4-4z" fill="#1db04b"/></svg>Holon</li>
  <li><svg width="8" height="11" viewBox="0 0 8 11"><path d="M4 0a4 4 0 0 1 4 4c0 3-4 7-4 7S0 7 0 4a4 4 0 0 1 4-4z" fill="#1db04b"/></svg>Jerusalem</li>
</ul>
<div class="btn btn--teal branches__btn">View All</div>
<div class="abs branches__frame"><div class="branches__img" role="img" aria-label="Photo of smiling volunteers in blue shirts holding a donation box"></div></div>

<!-- news -->
<div class="abs eyebrow news__eyebrow">Recent News</div>
<h2 class="abs news__title">Latest articles</h2>
<article class="article" style="left:223px">
  <div class="article__img" role="img" aria-label="Photo of a group hiking along a trail" style="background:linear-gradient(170deg,#9fb2b8,#6f8a7a 55%,#4a6a8e)"></div>
  <div class="article__body"><h3>Lorem Ipsum is simply<br>dummy text of the printing</h3><p>Lorem Ipsum has been the industry's standard dummy text ever since the 1500s, printer took a galley ...</p><div class="more">Read More →</div></div>
</article>
<article class="article" style="left:482px">
  <div class="article__img" role="img" aria-label="Photo of wheelchair users at an outdoor event" style="background:linear-gradient(170deg,#c7c98a,#7c8a5c 55%,#5a5a6a)"></div>
  <div class="article__body"><h3>Lorem Ipsum is simply<br>dummy text of the printing</h3><p>Lorem Ipsum has been the industry's standard dummy text ever since the 1500s, printer took a galley ...</p><div class="more">Read More →</div></div>
</article>
<article class="article" style="left:741px">
  <div class="article__img" role="img" aria-label="Photo of a beach wheelchair on the sand" style="background:linear-gradient(170deg,#8ec3e0,#c9d9e0 55%,#d9a24a)"></div>
  <div class="article__body"><h3>Lorem Ipsum is simply<br>dummy text of the printing</h3><p>Lorem Ipsum has been the industry's standard dummy text ever since the 1500s, printer took a galley ...</p><div class="more">Read More →</div></div>
</article>
<div class="btn news__btn">View All</div>

<!-- footer -->
<div class="abs footer"></div>
<div class="abs quote"></div>
<div class="abs quote__eyebrow">Get In Touch</div>
<h2 class="abs quote__title">Get a free quote</h2>
<div class="field" style="left:359px;top:3382px;width:235px;height:35px">Name</div>
<div class="field" style="left:604px;top:3382px;width:235px;height:35px">Phone</div>
<div class="field" style="left:359px;top:3431px;width:480px;height:35px">Email Address</div>
<div class="field" style="left:359px;top:3476px;width:480px;height:63px">Message...</div>
<div class="btn quote__btn">Submit</div>

<div class="abs footer__logo"><span></span>OREV</div>
<div class="footer__col" style="left:400px">
  <div class="footer__head">Contact Us</div>
  <ul class="footer__contact">
    <li><span style="color:var(--green)">✆</span>03-5550142</li>
    <li style="margin-top:8px"><span style="color:var(--green)">✆</span>03-5550187</li>
    <li><span style="color:var(--green)">✉</span>hello@orev-example.org</li>
    <li><svg width="8" height="11" viewBox="0 0 8 11"><path d="M4 0a4 4 0 0 1 4 4c0 3-4 7-4 7S0 7 0 4a4 4 0 0 1 4-4z" fill="#1db04b"/></svg><span>12 Cedar Lane, PO<br>Box 4410<br>Meadowfield 4900001</span></li>
  </ul>
</div>
<div class="footer__col" style="left:600px">
  <div class="footer__head">Quick Links</div>
  <ul class="footer__links"><li>Home</li><li>About</li><li>Programs</li><li>Rehabilitation &amp; Sports</li><li>Rights Realization</li><li>News</li><li>Contact Us</li></ul>
</div>
<div class="footer__col" style="left:727px;top:3741px">
  <ul class="footer__links" style="margin-top:0"><li>Term &amp; Conditions</li><li>Privacy Policy</li></ul>
</div>
<div class="footer__col" style="left:874px">
  <div class="footer__head">Follow Us</div>
  <div class="footer__social"><span></span><span></span><span></span></div>
</div>
<div class="abs copyright">© 2023 <b>Orev Association</b>. All Right Reserved &nbsp; | &nbsp; Accessibility Statement</div>

</body>
</html>
```